Christmas Ballet Poster for La Marioneta

I urgently need a poster for the La Marioneta ballet, it needs to look magical and very similar to the reference attached. The title should be La Marioneta and the typography and look should be as similar as possible as the words Winter Lantern in the reference attached. Use a dancers photo just for reference, I will not use that photo as someone will be taking the picture of the principal dancer and we will be using that. It should look magical, upscale and pretty.
Requirements
Must have
- Title: La Marioneta
- Space for date, time and prices
- Space to add logo
- It must look as similar as the reference as possible, magical, elegant.
Should not have
- Any logo

```html
<!DOCTYPE html>
<html lang="es">
<head>
<meta charset="utf-8">
<title>La Marioneta — Ballet de Navidad</title>
<link rel="stylesheet" href="https://fonts.googleapis.com/css2?family=Cinzel+Decorative:wght@700;900&family=Open+Sans:wght@600;700&display=swap">
<style>
  :root {
    --night-deep: #040a28;
    --night-mid: #0f2470;
    --stage-blue: #2f56c2;
    --curtain-blue: #4a78e0;
    --tutu-white: rgba(236, 242, 252, 0.85);
    --corps-white: rgba(200, 215, 245, 0.45);
    --ice-title: #dbe7ff;
    --ice-glow: rgba(150, 185, 255, 0.85);
    --text-white: #ffffff;
  }

  html, body {
    margin: 0;
    padding: 0;
    width: 1200px;
    height: 584px;
    overflow: hidden;
    background: var(--night-deep);
  }

  .poster {
    position: relative;
    width: 1200px;
    height: 584px;
    overflow: hidden;
    font-family: "Open Sans", Arial, sans-serif;
    color: var(--text-white);
  }

  .stage-photo {
    position: absolute;
    inset: 0;
    background:
      /* principal couple */
      radial-gradient(ellipse 90px 130px at 300px 260px, var(--tutu-white), rgba(236, 242, 252, 0) 75%),
      radial-gradient(ellipse 70px 200px at 250px 420px, rgba(225, 232, 250, 0.6), rgba(225, 232, 250, 0) 75%),
      radial-gradient(ellipse 140px 60px at 150px 280px, rgba(225, 232, 250, 0.35), rgba(225, 232, 250, 0) 75%),
      /* corps de ballet */
      radial-gradient(ellipse 70px 190px at 30px 390px, var(--corps-white), rgba(200, 215, 245, 0) 75%),
      radial-gradient(ellipse 70px 150px at 520px 420px, rgba(190, 205, 240, 0.3), rgba(190, 205, 240, 0) 75%),
      radial-gradient(ellipse 60px 130px at 1110px 450px, rgba(180, 195, 235, 0.22), rgba(180, 195, 235, 0) 75%),
      radial-gradient(ellipse 50px 110px at 1030px 470px, rgba(180, 195, 235, 0.16), rgba(180, 195, 235, 0) 75%),
      /* snowy stage light */
      radial-gradient(ellipse 380px 260px at 200px 110px, var(--curtain-blue), rgba(74, 120, 224, 0) 75%),
      radial-gradient(ellipse 620px 420px at 360px 320px, var(--stage-blue), rgba(47, 86, 194, 0) 80%),
      radial-gradient(ellipse 700px 480px at 820px 300px, var(--night-mid), rgba(15, 36, 112, 0) 85%),
      linear-gradient(180deg, #0b1c5c 0%, var(--night-deep) 100%);
  }

  .stage-photo::after {
    content: "";
    position: absolute;
    inset: 0;
    background: linear-gradient(90deg, rgba(4, 10, 40, 0) 45%, rgba(4, 10, 40, 0.3) 100%);
  }

  .sponsor {
    position: absolute;
    top: 44px;
    left: 915px;
    display: flex;
    align-items: center;
    gap: 12px;
    font-weight: 700;
    font-size: 48px;
    line-height: 1;
    color: var(--text-white);
  }

  .sponsor-mark {
    width: 22px;
    height: 22px;
    border-radius: 50%;
    background: var(--text-white);
  }

  .title {
    position: absolute;
    left: 420px;
    top: 190px;
    width: 740px;
    margin: 0;
    display: flex;
    align-items: baseline;
    font-family: "Cinzel Decorative", "Times New Roman", serif;
    font-weight: 900;
    color: var(--ice-title);
    text-shadow: 0 0 6px var(--ice-glow), 0 0 18px rgba(120, 160, 255, 0.6);
    white-space: nowrap;
  }

  .title-article {
    display: inline-block;
    font-size: 56px;
    margin-right: 12px;
    transform: rotate(-6deg);
  }

  .title-name {
    font-size: 84px;
    letter-spacing: 1px;
  }

  .title-initial {
    font-size: 150px;
    line-height: 0.8;
  }

  .show-time {
    position: absolute;
    left: 760px;
    top: 374px;
    margin: 0;
    font-weight: 600;
    font-size: 31px;
    line-height: 1.2;
    white-space: nowrap;
    color: var(--text-white);
  }

  .divider {
    margin: 0 18px;
  }
</style>
</head>
<body>
  <main class="poster">
    <div class="stage-photo" role="img" aria-label="Photograph of a ballerina in a white tutu held by her partner in an arabesque, with corps de ballet dancers in white behind them on a deep blue stage filled with falling snow and sparkles"></div>

    <div class="sponsor">
      <span class="sponsor-mark"></span>
      <span class="sponsor-name">nimbus</span>
    </div>

    <h1 class="title">
      <span class="title-article">LA</span>
      <span class="title-name"><span class="title-initial">M</span>ARIONETA</span>
    </h1>

    <p class="show-time">14 Nov. 2018<span class="divider">|</span>10.00 pm</p>
  </main>
</body>
</html>
```